Flyer-Design für Wäscherei sucht Design
Zielgruppe
Wir sind eine Wäscherei.
Zielgruppe: Kunden aus der Hotel- und Gastronomiebranche
Aufgabenstellung
Wir benötigen einen 2-seitigen Flyer DIN lang. 9,8 x21cm
TextInhalte sind in der Vorlage-Datei.
Bilder sind eingefügt.

```html
<!DOCTYPE html>
<html lang="de">
<head>
<meta charset="utf-8">
<title>Serviettenfaltservice – Wäscherei Brenner</title>
<link rel="stylesheet" href="https://fonts.googleapis.com/css2?family=Source+Sans+3:wght@400;600;700&display=swap">
<style>
  :root {
    --magenta: #c3007a;
    --ink: #1d1d1b;
    --paper: #ffffff;
    --photo-dark: #3a3d44;
    --photo-light: #c9c8c6;
  }
  * { margin: 0; padding: 0; box-sizing: border-box; }
  html, body { width: 1200px; height: 560px; overflow: hidden; background: var(--paper); }
  body { font-family: "Source Sans 3", Arial, sans-serif; color: var(--ink); }
  .flyer { position: relative; width: 1200px; height: 560px; }

  .headline { position: absolute; left: 56px; top: 55px; padding-left: 35px; }
  .headline::before {
    content: ""; position: absolute; left: 0; top: 2px; width: 12px; height: 43px; background: var(--magenta);
  }
  .headline h1 { font-size: 22px; font-weight: 700; color: var(--magenta); line-height: 24px; letter-spacing: .2px; }
  .headline p { font-size: 21px; color: var(--magenta); line-height: 25px; }

  .intro { position: absolute; left: 57px; top: 126px; font-size: 17.5px; line-height: 24.3px; }

  .prices { position: absolute; left: 57px; top: 247px; display: flex; }
  .price { font-size: 17.5px; line-height: 24.3px; }
  .price:first-child { width: 314px; }
  .price strong { font-weight: 700; }

  .details { position: absolute; left: 57px; top: 344px; font-size: 17.5px; line-height: 24.3px; }
  .note { position: absolute; left: 57px; top: 424px; font-size: 11px; }

  .contact { position: absolute; left: 57px; top: 490px; display: flex; align-items: center; gap: 7px; font-size: 12.5px; }
  .contact .brand { font-weight: 700; color: var(--magenta); font-size: 12px; margin-right: 4px; }
  .contact .sep { width: 4px; height: 4px; background: var(--magenta); transform: rotate(45deg); }
  .contact svg { display: block; }

  .photo { position: absolute; left: 808px; width: 392px; }
  .photo-top { top: 0; height: 181px; background: linear-gradient(180deg, #2c2f36 0%, #6b6a68 45%, var(--photo-light) 100%); }
  .photo-bottom { top: 191px; height: 369px; background: radial-gradient(circle at 30% 20%, #6a4a8c 0%, #2a1f3a 40%, #8c8a90 75%, #d9d7d8 100%); }
</style>
</head>
<body>
<main class="flyer">
  <header class="headline">
    <h1>IHR SERVIETTENFALTSERVICE</h1>
    <p>ab November 2017</p>
  </header>

  <section class="intro">
    <p>Wir optimieren Ihren Serviettenfaltprozess.</p>
    <p>Wir entlasten Sie von dieser demotivierenden und unproduktiven Tätigkeit.</p>
    <p>Wir falten Ihnen Ihre Stoffservietten oder unsere Mietservietten vor.</p>
    <p>Hygienisch, zuverlässig und wirtschaftlich – bereit für die Mise en Place.</p>
  </section>

  <section class="prices">
    <div class="price">
      <p>Faltformen – Kategorie 1:</p>
      <p><strong>Welle, Kerze, Fächer</strong></p>
      <p>je Faltung für nur 0,20 € *</p>
    </div>
    <div class="price">
      <p>Faltformen – Kategorie 2:</p>
      <p><strong>Pyramide, Bischofsmütze</strong></p>
      <p>je Faltung für nur 0,35 € *</p>
    </div>
  </section>

  <section class="details">
    <p>Weitere Formen sind auf Anfrage möglich.</p>
    <p>Bei Bedarf stellen wir Ihnen Mietservietten für nur 0,25 €* je Stück zur Verfügung.</p>
    <p>Mindestabnahmemenge: 100 Stück</p>
  </section>
  <p class="note">*zzgl. gesetzliche MwSt.</p>

  <footer class="contact">
    <span class="brand">WÄSCHEREI BRENNER</span>
    <span>Wäscherei Brenner</span><span class="sep"></span>
    <span>Lindenweg 12</span><span class="sep"></span>
    <span>71634 Talbach</span>
    <svg width="11" height="11" viewBox="0 0 24 24" aria-hidden="true"><path fill="#c3007a" d="M6.6 10.8a15 15 0 0 0 6.6 6.6l2.2-2.2c.3-.3.7-.4 1-.2 1.1.4 2.3.6 3.6.6.6 0 1 .4 1 1V20c0 .6-.4 1-1 1C10.6 21 3 13.4 3 4c0-.6.4-1 1-1h3.5c.6 0 1 .4 1 1 0 1.3.2 2.5.6 3.6.1.3 0 .7-.2 1z"/></svg>
    <span>+49 (0) 7000 / 12 34 56</span>
    <svg width="12" height="10" viewBox="0 0 24 18" aria-hidden="true"><rect x="1.5" y="1.5" width="21" height="15" fill="none" stroke="#c3007a" stroke-width="3"/><path d="M2 2l10 8 10-8" fill="none" stroke="#c3007a" stroke-width="3"/></svg>
    <span>info@waescherei-brenner.de</span>
  </footer>

  <div class="photo photo-top" role="img" aria-label="Festlich gedeckter Restauranttisch mit Gläsern und gefalteten Servietten"></div>
  <div class="photo photo-bottom" role="img" aria-label="Weingläser und gefaltete weiße Servietten vor farbigem Bokeh-Hintergrund"></div>
</main>
</body>
</html>
```